need 4 creative A frame (SANDWICH BOARD) designs concepts for dental office

need 4 creative A frame (SANDWICH BOARD) designs concepts
1 - targeting kids
2. targeting old age
3. targeting teens
4 targeting general public

website - www.brenvaxdental.ca

LINK for Measurements for sandwich board https://www.korvepa.ca/BL_1921/Aluminum-Snap-Edge-A-Frame-Sign

i am attaching certain key ingredients ( rough sketch in uploaded files ) to be added on each design though not mandatory if the design is very creative

```html
<!DOCTYPE html>
<html lang="en">
<head>
<meta charset="utf-8">
<title>Brenvax Dental – A-Frame Board</title>
<link rel="stylesheet" href="https://fonts.googleapis.com/css2?family=Quicksand:wght@300;400;700&family=Arimo:wght@400;700&display=swap">
<style>
  :root {
    --paper: #ffffff;
    --slate: #6d6f73;
    --sky: #4ac3e8;
    --sky-deep: #1a86b3;
    --mist: #c9cacc;
    --brand-grey: #8c8d8f;
    --ink: #000000;
    --photo-light: #d3e2e6;
    --photo-mid: #a9c2cf;
    --photo-warm: #b9785a;
  }
  html, body {
    margin: 0;
    padding: 0;
    overflow: hidden;
    background: var(--paper);
  }
  .board {
    position: relative;
    width: 943px;
    height: 1200px;
    overflow: hidden;
    background: var(--paper);
  }
  .board-art {
    display: block;
    width: 943px;
    height: 1200px;
  }
  .slate-band { fill: var(--slate); }
  .badge-ring { fill: var(--paper); }
  .badge-disc { fill: var(--sky); }
  .badge-label {
    font-family: "Arimo", Arial, sans-serif;
    font-weight: 700;
    font-size: 50px;
    fill: var(--sky-deep);
  }
  .badge-chevron { fill: var(--paper); }
  .headline-lead {
    font-family: "Quicksand", sans-serif;
    font-weight: 400;
    font-size: 74px;
    fill: var(--paper);
  }
  .headline-word {
    font-family: "Quicksand", sans-serif;
    font-weight: 400;
    font-size: 200px;
    fill: var(--paper);
    letter-spacing: 2px;
  }
  .tagline {
    font-family: "Quicksand", sans-serif;
    font-size: 62px;
    fill: var(--mist);
  }
  .tagline-light { font-weight: 400; }
  .tagline-bold { font-weight: 700; }
  .brand-name {
    font-family: "Quicksand", sans-serif;
    font-weight: 700;
    font-size: 150px;
    fill: var(--brand-grey);
  }
  .patients-pill { fill: var(--ink); }
  .patients-label {
    font-family: "Arimo", Arial, sans-serif;
    font-weight: 400;
    font-size: 52px;
    fill: var(--paper);
  }
  .phone {
    font-family: "Arimo", Arial, sans-serif;
    font-weight: 700;
    fill: var(--sky);
  }
  .phone-area { font-size: 72px; }
  .phone-main { font-size: 118px; }
</style>
</head>
<body>
<main class="board">
  <svg class="board-art" viewBox="0 0 1500 1909" xmlns="http://www.w3.org/2000/svg">
    <defs>
      <radialGradient id="portrait-tone" cx="0.55" cy="0.45" r="0.6">
        <stop offset="0" stop-color="var(--photo-warm)" stop-opacity="0.55"/>
        <stop offset="0.45" stop-color="var(--photo-light)"/>
        <stop offset="1" stop-color="var(--photo-mid)"/>
      </radialGradient>
    </defs>

    <path class="slate-band" d="M0 0 H1500 V1195 C1250 1300 900 1320 600 1245 C350 1175 120 900 0 690 Z"/>

    <circle class="portrait" cx="955" cy="265" r="650" fill="url(#portrait-tone)"
            role="img" aria-label="Photo of a smiling woman with long auburn hair resting her chin on her hand"/>

    <g class="badge">
      <circle class="badge-ring" cx="265" cy="992" r="198"/>
      <circle class="badge-disc" cx="265" cy="992" r="182"/>
      <text class="badge-label" x="265" y="926" text-anchor="middle">WE’RE IN</text>
      <polygon class="badge-chevron" points="180,955 245,955 173,1029 245,1103 180,1103 106,1029"/>
      <polygon class="badge-chevron" points="265,955 330,955 258,1029 330,1103 265,1103 191,1029"/>
      <polygon class="badge-chevron" points="345,955 410,955 338,1029 410,1103 345,1103 271,1029"/>
    </g>

    <g class="headline">
      <text class="headline-lead" x="506" y="1070">Make a</text>
      <text class="headline-word" x="770" y="1068">smile</text>
      <text class="tagline" x="1230" y="1143" text-anchor="end"><tspan class="tagline-light">your </tspan><tspan class="tagline-bold">signature</tspan></text>
      <text class="tagline tagline-bold" x="1335" y="1207" text-anchor="end">accessory</text>
    </g>

    <text class="brand-name" x="750" y="1470" text-anchor="middle">Brenvax Dental</text>

    <rect class="patients-pill" x="382" y="1645" width="736" height="83" rx="41.5"/>
    <text class="patients-label" x="750" y="1705" text-anchor="middle">Accepting New Patients</text>

    <text class="phone" x="750" y="1850" text-anchor="middle"><tspan class="phone-area">587 </tspan><tspan class="phone-main">555 0142</tspan></text>
  </svg>
</main>
</body>
</html>
```